Supplement Rebranding Bottle Design

READ WORD DOCUMENT ATTACHED.
We want to rebrand our current health supplements (see below). We do want it to be modern, vibrant and appealing. Very upscale and elegant as it targets primarily women.
Bottle size: see pictures for bottle size, along with sample bottles that we like; we’re open to any bottle similar to the ones attached.
Current bottles: So ideally, we’d keep the core color on each bottle with a new branding/bottle design. But we're open to your suggestion.

Target Market(s)

mostly women but shouldn't be overly feminine

Requirements
Must have
• see bottle sizes attached

```html
<!DOCTYPE html>
<html lang="en">
<head>
<meta charset="utf-8">
<title>Axis Supplement Range</title>
<link rel="stylesheet" href="https://fonts.googleapis.com/css2?family=Roboto:wght@400;500;700&display=swap">
<style>
  :root {
    --canvas: #ffffff;
    --ink: #ffffff;
    --liver: #8a2ea3;
    --liver-lid: #9a33b5;
    --tummy: #e1302b;
    --tummy-lid: #e8332d;
    --hormone: #2ea33b;
    --hormone-lid: #34b042;
    --sugar: #3d62b0;
    --sugar-lid: #4468b6;
  }
  html, body {
    margin: 0;
    width: 959px;
    height: 1200px;
    overflow: hidden;
    background: var(--canvas);
    font-family: "Roboto", Arial, sans-serif;
    color: var(--ink);
  }
  .range { position: relative; width: 959px; height: 1200px; }
  .jar { position: absolute; width: 268px; height: 440px; }
  .jar--liver   { left: 133px; top: 162px; --body: var(--liver);   --lid: var(--liver-lid); }
  .jar--tummy   { left: 571px; top: 162px; --body: var(--tummy);   --lid: var(--tummy-lid); }
  .jar--hormone { left: 133px; top: 666px; --body: var(--hormone); --lid: var(--hormone-lid); }
  .jar--sugar   { left: 571px; top: 666px; --body: var(--sugar);   --lid: var(--sugar-lid); }

  .lid {
    position: absolute; left: 0; top: 0; width: 268px; height: 72px;
    background: var(--lid);
    border-radius: 6px 6px 2px 2px;
  }
  .lid-grip {
    position: absolute; left: 0; right: 0; top: 14px; height: 58px;
    background: repeating-linear-gradient(90deg, rgba(0,0,0,0.12) 0 2px, transparent 2px 10px);
  }
  .body {
    position: absolute; left: 4px; top: 72px; width: 260px; height: 368px;
    background: var(--body);
    border-radius: 0 0 26px 26px;
  }
  .brand {
    position: absolute; left: 0; right: 0; top: 80px;
    margin: 0; text-align: center;
    font-weight: 700; font-size: 25px; line-height: 30px; letter-spacing: -0.5px;
  }
  .claim {
    position: absolute; left: 0; right: 0; top: 160px; margin: 0;
    text-align: center; font-weight: 500; font-size: 14px; line-height: 19px;
    text-transform: uppercase; letter-spacing: 0.3px;
  }
  .count-box {
    position: absolute; left: 50%; top: 235px; transform: translateX(-50%);
    display: flex; border: 1px solid var(--ink); height: 35px;
  }
  .count {
    display: flex; flex-direction: column; align-items: center; justify-content: center;
    padding: 0 4px; border-right: 1px solid var(--ink);
  }
  .count-number { font-weight: 700; font-size: 16px; line-height: 15px; }
  .count-unit { font-size: 5px; line-height: 5.5px; text-align: center; font-weight: 500; }
  .count-label { padding: 2px 6px 0; font-size: 12.5px; line-height: 13px; }
  .rule {
    position: absolute; left: 20px; right: 26px; top: 290px; height: 1.5px; background: var(--ink);
  }
  .volume {
    position: absolute; left: 0; right: 0; top: 308px;
    text-align: center; font-size: 7px; font-weight: 700;
  }
</style>
</head>
<body>
<main class="range">

  <section class="jar jar--liver">
    <div class="lid"><div class="lid-grip"></div></div>
    <div class="body">
      <h2 class="brand">LiverAxis</h2>
      <p class="claim">Rejuvenating Cleanse<br>&amp; Detox Formula</p>
      <div class="count-box">
        <div class="count"><span class="count-number">120</span><span class="count-unit">Vegetable<br>Capsules</span></div>
        <div class="count-label">Dietary<br>Supplement</div>
      </div>
      <div class="rule"></div>
      <div class="volume">100 ml</div>
    </div>
  </section>

  <section class="jar jar--tummy">
    <div class="lid"><div class="lid-grip"></div></div>
    <div class="body">
      <h2 class="brand">TummyAxis</h2>
      <p class="claim">Oxygenating Colon<br>Cleanse</p>
      <div class="count-box">
        <div class="count"><span class="count-number">90</span><span class="count-unit">Vegetable<br>Capsules</span></div>
        <div class="count-label">Dietary<br>Supplement</div>
      </div>
      <div class="rule"></div>
      <div class="volume">100 ml</div>
    </div>
  </section>

  <section class="jar jar--hormone">
    <div class="lid"><div class="lid-grip"></div></div>
    <div class="body">
      <h2 class="brand">HormoneAxis</h2>
      <p class="claim">Supports Healthy<br>Hormone Levels</p>
      <div class="count-box">
        <div class="count"><span class="count-number">60</span><span class="count-unit">Vegetable<br>Capsules</span></div>
        <div class="count-label">Dietary<br>Supplement</div>
      </div>
      <div class="rule"></div>
      <div class="volume">100 ml</div>
    </div>
  </section>

  <section class="jar jar--sugar">
    <div class="lid"><div class="lid-grip"></div></div>
    <div class="body">
      <h2 class="brand">Blood Sugar Axis</h2>
      <p class="claim">Supports Healthy<br>Blood Glucose Levels</p>
      <div class="count-box">
        <div class="count"><span class="count-number">60</span><span class="count-unit">Vegetable<br>Capsules</span></div>
        <div class="count-label">Dietary<br>Supplement</div>
      </div>
      <div class="rule"></div>
      <div class="volume">100 ml</div>
    </div>
  </section>

</main>
</body>
</html>
```